Billboard Design

Billboard design featuring the colors dark teal and dark grey.
Company: Cedarbrook Hollow Properties
Services Real Estate & Management
Phone: 614-739-5081
Important info:
Professionalizing Property Management
Specialized training and credentials in Property Management
Serving single family, multifamily, complexes, and mixed use properties.

UPDATE: We have uploaded photos from a recent project of ours and would love to see them used on the billboard.

```html
<!DOCTYPE html>
<html lang="en">
<head>
<meta charset="utf-8">
<title>Cedarbrook Hollow Properties — Billboard</title>
<link href="https://fonts.googleapis.com/css2?family=Libre+Baskerville:wght@700&family=Crimson+Pro:wght@500;600&display=swap" rel="stylesheet">
<style>
  :root {
    --teal: #00777a;
    --teal-deep: #00686b;
    --grey-dark: #4a4a4c;
    --grey-mid: #5b5b5e;
    --white: #ffffff;
    --ink: #333335;
    --stage: #6e6e70;
  }
  * { margin: 0; padding: 0; box-sizing: border-box; }
  html, body {
    width: 1056px; height: 1200px; overflow: hidden;
    background: var(--stage);
  }
  .canvas {
    position: relative; width: 1056px; height: 1200px;
  }
  .billboard {
    position: absolute; left: 28px; top: 443px;
    width: 1000px; height: 312px;
    filter: drop-shadow(0 10px 14px rgba(0,0,0,.4));
  }
  .headline {
    font-family: "Libre Baskerville", Georgia, serif;
    font-weight: 700; font-size: 76px; fill: var(--white);
  }
  .brand-name {
    font-family: "Crimson Pro", Georgia, serif;
    font-weight: 600; font-size: 44px; fill: var(--ink);
  }
  .benefit {
    font-family: "Crimson Pro", Georgia, serif;
    font-weight: 500; font-size: 27px; fill: var(--white);
  }
  .phone-number {
    font-family: "Crimson Pro", Georgia, serif;
    font-weight: 600; font-size: 70px; fill: var(--white);
    letter-spacing: 2px;
  }
  .icon-line { fill: none; stroke: var(--white); stroke-width: 2; }
</style>
</head>
<body>
<div class="canvas">
  <svg class="billboard" viewBox="0 0 1578 492" xmlns="http://www.w3.org/2000/svg">
    <defs>
      <linearGradient id="kitchenTones" x1="0" y1="0" x2="1" y2="1">
        <stop offset="0" stop-color="#d9d6d0"/>
        <stop offset="0.45" stop-color="#8a8884"/>
        <stop offset="0.7" stop-color="#e9e5df"/>
        <stop offset="1" stop-color="#a0927e"/>
      </linearGradient>
      <linearGradient id="roomTones" x1="0" y1="0" x2="0" y2="1">
        <stop offset="0" stop-color="#e4e2dd"/>
        <stop offset="0.55" stop-color="#9c9a96"/>
        <stop offset="1" stop-color="#7a6a58"/>
      </linearGradient>
    </defs>

    <!-- base -->
    <rect class="billboard-base" width="1578" height="492" fill="var(--teal)"/>

    <!-- project photo area -->
    <rect class="project-photo" x="520" y="90" width="1058" height="340" fill="url(#kitchenTones)"
          role="img" aria-label="Photo of a renovated kitchen with white cabinets, stainless appliances and a sink"/>

    <!-- white brand area -->
    <path class="brand-panel" d="M0 150 L560 95 L560 300 C420 335 220 345 0 325 Z" fill="var(--white)"/>

    <!-- headline band -->
    <path class="headline-band" d="M0 0 H1578 V98 C1420 135 1180 140 900 128 C700 118 430 108 0 176 Z" fill="var(--teal)"/>
    <path class="headline-accent" d="M820 130 C760 128 730 128 700 130 L745 150 Z" fill="var(--grey-dark)"/>

    <!-- phone band -->
    <path class="phone-band" d="M930 402 C1040 378 1250 368 1578 372 V492 H1060 C1010 450 975 425 930 402 Z" fill="var(--grey-dark)"/>

    <!-- lower teal band -->
    <path class="info-band-edge" d="M0 318 C220 338 420 330 560 282 L760 322 C860 338 960 400 1075 492 H0 Z" fill="var(--grey-mid)"/>
    <path class="info-band" d="M0 326 C220 346 420 338 560 292 L760 332 C850 346 940 404 1040 492 H0 Z" fill="var(--teal)"/>

    <!-- circular project photo -->
    <circle cx="650" cy="258" r="138" fill="none" stroke="var(--teal-deep)" stroke-width="2"/>
    <circle class="project-photo-round" cx="654" cy="258" r="128" fill="url(#roomTones)"
            role="img" aria-label="Photo of an open-plan kitchen and entry with wood-look flooring"/>

    <!-- headline -->
    <text class="headline" x="789" y="88" text-anchor="middle" textLength="1440" lengthAdjust="spacing">REAL ESTATE &amp; MANAGEMENT</text>

    <!-- brand name -->
    <text class="brand-name" x="300" y="214" text-anchor="middle">Cedarbrook Hollow</text>
    <text class="brand-name" x="300" y="260" text-anchor="middle">Properties</text>

    <!-- benefits -->
    <g class="benefit-list">
      <g transform="translate(86 363)">
        <circle class="icon-line" r="10"/><path class="icon-line" d="M-5 0 L-1 4 L5 -4"/>
      </g>
      <text class="benefit" x="110" y="372">Professionalizing Property Management</text>
      <g transform="translate(86 402)">
        <circle class="icon-line" r="10"/><path class="icon-line" d="M-5 0 L-1 4 L5 -4"/>
      </g>
      <text class="benefit" x="110" y="411">Specialized training and credentials in Property Management</text>
      <g transform="translate(86 441)">
        <circle class="icon-line" r="10"/><path class="icon-line" d="M-5 0 L-1 4 L5 -4"/>
      </g>
      <text class="benefit" x="110" y="450">Serving single family, multifamily, complexes, and mixed use properties.</text>
    </g>

    <!-- phone -->
    <g class="phone-icon" transform="translate(1052 433)">
      <circle r="26" fill="none" stroke="var(--white)" stroke-width="3"/>
      <path d="M-9 -14 L-3 -14 L0 -6 L-4 -2 C-2 3 1 6 5 8 L9 4 L16 7 L16 12 C16 15 13 17 10 16 C-3 12 -12 3 -15 -10 C-16 -13 -13 -14 -9 -14 Z" fill="var(--white)"/>
    </g>
    <text class="phone-number" x="1096" y="457">614-739-5081</text>
  </svg>
</div>
</body>
</html>
```